Bellucari Wine label**

Hi, we need a design for a white, red and sparkling wine label. We are a small italian restaurant (Bellucari) and we want to release some wines under our personal brand. The restaurant has a rustic, italian provance style with with a slight modern, clean lines look. We would like a design that represent our mission to provide as authentic Italian food as we can, something that feels that it has been brought from the heart of Italy.
https://www.bellucaricafe.example/

```html
<!DOCTYPE html>
<html lang="en">
<head>
<meta charset="utf-8">
<title>Bellucari Bordeaux Wine Label</title>
<link rel="stylesheet" href="https://fonts.googleapis.com/css2?family=Playfair+Display:wght@400;700&family=Parisienne&display=swap">
<style>
  :root {
    --backdrop: #efefef;
    --label-paper: #faf4e8;
    --wine-red: #a4222d;
    --deep-red: #8a1a24;
    --ink: #2a1719;
    --sketch-light: #e9e0d2;
    --sketch-dark: #8d7f78;
  }
  * { margin: 0; padding: 0; box-sizing: border-box; }
  html, body {
    width: 1200px; height: 900px; overflow: hidden;
    background: var(--backdrop);
  }
  .canvas {
    position: relative; width: 1200px; height: 900px;
  }
  .wine-label {
    position: absolute; left: 390px; top: 24px;
    width: 420px; height: 852px;
    background: var(--label-paper);
    font-family: "Playfair Display", Georgia, serif;
    color: var(--ink);
  }
  .label-lines {
    position: absolute; inset: 0; width: 420px; height: 852px;
  }
  .estate-mark {
    position: absolute; left: 198px; top: 28px;
    width: 22px; height: 22px; border-radius: 50%;
    background: var(--wine-red);
  }
  .founding-year {
    position: absolute; left: 0; right: 0; top: 50px;
    display: flex; justify-content: center; gap: 44px;
    font-size: 10px; letter-spacing: 6px; color: var(--wine-red);
  }
  .appellation {
    position: absolute; left: 0; right: 0; top: 84px;
    text-align: center; font-size: 12px; letter-spacing: 2px;
    color: var(--ink);
  }
  .vineyard-scene {
    position: absolute; left: 24px; top: 122px; width: 374px; height: 206px;
    border-radius: 50% 50% 40% 40% / 30% 30% 70% 70%;
    background: radial-gradient(ellipse at 50% 55%, var(--sketch-dark) 0%, var(--sketch-light) 62%, var(--label-paper) 80%);
    opacity: 0.75;
  }
  .wine-name {
    position: absolute; left: 0; right: 0; top: 414px;
    text-align: center; font-weight: 700; font-size: 50px;
    letter-spacing: -1px; color: var(--ink);
  }
  .origin-note {
    position: absolute; left: 0; right: 0; top: 478px;
    text-align: center; font-family: "Parisienne", cursive;
    font-size: 21px; color: var(--wine-red);
  }
  .vintage {
    position: absolute; left: 0; right: 0; top: 532px;
    text-align: center; font-size: 28px; letter-spacing: 3px;
    color: var(--ink);
  }
  .vintage-flourish {
    position: absolute; left: 162px; top: 574px; width: 96px; height: 10px;
    border-radius: 5px; background: var(--wine-red); opacity: 0.55;
  }
  .quality-seal {
    position: absolute; left: 159px; top: 619px; width: 100px; height: 100px;
    border-radius: 50%; background: var(--wine-red);
    box-shadow: inset 0 0 0 5px var(--deep-red);
  }
  .brand-band {
    position: absolute; left: 21px; top: 736px; width: 375px; height: 76px;
    background: var(--wine-red);
    display: flex; align-items: center; justify-content: center;
  }
  .brand-name {
    font-family: "Playfair Display", Georgia, serif;
    font-weight: 400; font-size: 30px; letter-spacing: 8px;
    color: var(--label-paper);
  }
</style>
</head>
<body>
<main class="canvas">
  <section class="wine-label">
    <svg class="label-lines" viewBox="0 0 420 852" aria-hidden="true">
      <g fill="none" stroke="var(--wine-red)">
        <path d="M24 300 V672 H395 V300 Q209 390 24 300 Z" stroke-width="3"/>
        <path d="M33 316 V663 H386 V316 Q209 400 33 316 Z" stroke-width="1.5"/>
        <line x1="21" y1="726" x2="396" y2="726" stroke-width="2.5"/>
        <line x1="21" y1="822" x2="396" y2="822" stroke-width="2.5"/>
      </g>
    </svg>

    <div class="estate-mark"></div>
    <div class="founding-year"><span>19</span><span>78</span></div>
    <p class="appellation">VIN DE BOEDEAUX</p>

    <div class="vineyard-scene" role="img" aria-label="Engraved sketch of rolling vineyard hills with a farmhouse and cypress trees"></div>

    <h1 class="wine-name">BORDEAUX</h1>
    <p class="origin-note">Producto de Italia</p>
    <p class="vintage">2017</p>
    <div class="vintage-flourish" role="img" aria-label="Small decorative flourish under the vintage"></div>

    <div class="quality-seal" role="img" aria-label="Red wax quality seal"></div>

    <div class="brand-band">
      <span class="brand-name">Bellucari</span>
    </div>
  </section>
</main>
</body>
</html>
```